DL heavy card Flyer Design

Hi :) URGENTLY REQUIRED PLEASE We need a new and revised upbeat flyer design please….I feel like our current ones are dull and flat and don't really relate to our logo etc in any way…. the current flyer incorporates none of our logo and colour schemes associated with our branding….also they don't really have and graphics to catch peoples eye I want the new ones to be double sided and maybe thinking more in depth info about the services we provide but completely happy to go with your professional opinion :) The flyers will be printed in DL card size and mainly get slipped under the doors of new houses close to handover dateI have attached some images of other peoples flyer designs that i like the concept of if that helpsI have also attached a few images to illustrate the scope of works we conduct Im happy to use professional generic marketing images if it makes the flyers more appealing We are also on Facebook so you can get an idea of our business ( I'm also wanting to put the Facebook details on the front of the flyer somehow) please email me at stonvale@mailbox.example to discuss if requiredA bulrb from tradefindr.example- Highly professional and reliable concreters and landscapers with over 15 years of experience in the trade.About Elitecrete ConstructionsA reputable and established business in operation for over 10 years. We are backed by over 15 years of trade industry experience, making us your best choice for any concreting or landscaping work that you might require. We are passionate about what we do and this clearly shows through in the work we produce. We are also proud members of the Keystone Trades Guild.With us you get a high quality result that stands the test of time; we have superior attention to detail, we don't take shortcuts, and we always ensure that our concreting work is neat, tidy and suited to your home and its surrounds. We treat every job as if it is our own. We are focused on providing quality workmanship, outstanding service and value for your money with the highest level of customer service and customer satisfaction.Since every job is unique, we cater to different needs and tastes by offering a wide variety of options to choose from.Our servicesWe focus on both commercial and residential work. With us, no job is too big or too small.Our services include, but are not limited to:General concretingConcreting for new homes or renovationsConcreting for new home packagesFootpathsOutdoor patiosConcrete, timber and stone retaining wallsExcavation, post hole digging and earth moving needsExposed aggregate specialistsColour cove specialistsPool surroundsLandscapingLawn and turf layingQuotes straight from plansConcrete removalLandscape design and constructionProject managementWe are always happy to discuss your plans and ideas. Get in touch with us and have a chat about what the job is, what needs to be done and your preferred timeframe and we will work in conjunction with you to get you the results you desire. We will always try to work within your budget where possible. All our prices are based on current market rates. We are also happy to assist our clients in getting other work done, since we have great working relationships with our suppliers and a range of different trades. We really are a one stop shop.We usually charge per job and will always take everything into consideration to give you a fair and accurate quote.Our current hours are 6.30am - 8.30pm 7 days per week. We are very flexible with our schedule. https://www.social.example/Morvasta-Constructions-Pty-Ltd-…/

```html
<!DOCTYPE html>
<html lang="en">
<head>
<meta charset="utf-8">
<title>Morvasta Constructions – Services Flyer</title>
<link rel="stylesheet" href="https://fonts.googleapis.com/css2?family=Saira:wght@300;400&family=Teko:wght@500;600&display=swap">
<style>
  :root {
    --navy: #22409a;
    --gold: #f5c21b;
    --teal: #1ab59f;
    --teal-light: #7fd6cd;
    --circle-top: #00b3a8;
    --circle-bottom: #0b8a76;
    --ink: #1d1d1f;
    --backdrop: #e9ebec;
    --body: "Saira", "Helvetica Neue", Arial, sans-serif;
    --display: "Teko", "Oswald", sans-serif;
  }
  * { margin: 0; padding: 0; box-sizing: border-box; }
  html, body { width: 1200px; height: 1200px; overflow: hidden; background: var(--backdrop); }
  .flyer {
    position: absolute; left: 202px; top: 34px; width: 800px; height: 1128px;
    overflow: hidden; font-family: var(--body); font-weight: 300; color: #fff;
    background: linear-gradient(180deg, #ffffff 0%, #dde4ec 100%);
  }
  .services { position: absolute; left: 0; top: 0; width: 800px; height: 739px; background: var(--navy); }
  .services__title {
    position: absolute; left: 42px; top: 36px; font-family: var(--display); font-weight: 600;
    font-size: 34px; line-height: 36px; color: var(--gold); font-variant: small-caps; letter-spacing: .5px;
  }
  .services__intro { position: absolute; left: 42px; top: 75px; font-size: 16px; letter-spacing: .2px; white-space: nowrap; }
  .services__subtitle {
    position: absolute; left: 42px; top: 112px; font-family: var(--display); font-weight: 600;
    font-size: 25px; line-height: 28px; color: var(--gold); font-variant: small-caps; letter-spacing: .3px;
  }
  .service-list { position: absolute; top: 143px; list-style: none; font-size: 16px; line-height: 20.6px; letter-spacing: .2px; }
  .service-list--left { left: 74px; width: 330px; }
  .service-list--right { left: 472px; width: 320px; }
  .service-list li { position: relative; }
  .service-list li::before { content: "➲"; position: absolute; left: -28px; top: 0; font-size: 11px; }
  .pricing-band {
    position: absolute; left: 0; top: 346px; width: 800px; height: 66px;
    background: linear-gradient(90deg, rgba(26,181,159,0) 15%, rgba(26,150,170,.35) 45%, var(--teal) 100%);
  }
  .pricing-band p {
    position: absolute; right: 40px; top: 6px; text-align: right; font-size: 15px; line-height: 18.4px; white-space: nowrap;
  }
  .photo { position: absolute; top: 422px; height: 309px; }
  .photo--lawn { left: 0; width: 270px; background: linear-gradient(180deg, #c9d9e8 0%, #b9b3a6 40%, #5f9a3a 60%, #3f7a24 100%); }
  .photo--path { left: 278px; width: 267px; background: linear-gradient(180deg, #6b5a4e 0%, #b7aa98 35%, #8d8e90 60%, #7a7b7e 100%); }
  .photo--deck { left: 553px; width: 247px; background: linear-gradient(135deg, #7a8a4f 0%, #8c4a2a 40%, #a65a34 60%, #c8b89a 100%); }
  .contact-circle { position: absolute; left: 0; top: 0; }
  .contact-copy { position: absolute; left: 34px; font-size: 16px; line-height: 19.8px; letter-spacing: .15px; white-space: nowrap; }
  .contact-copy--chat { top: 762px; }
  .contact-copy--budget { top: 920px; }
  .chevrons { position: absolute; left: 466px; top: 814px; }
  .hours { position: absolute; left: 554px; top: 800px; color: var(--ink); font-weight: 400; }
  .hours__lead, .hours__note { font-size: 18px; line-height: 22px; letter-spacing: .2px; }
  .hours__time {
    font-family: var(--display); font-weight: 600; color: var(--navy); font-size: 31px; line-height: 25px;
    padding-top: 6px; letter-spacing: .3px;
  }
  .hours__note { margin-top: 2px; }
  .social { position: absolute; left: 533px; top: 1049px; display: flex; align-items: center; gap: 10px; color: var(--ink); }
  .social__mark { width: 32px; height: 32px; background: var(--navy); }
  .social__link { font-size: 15px; line-height: 16px; font-weight: 400; }
</style>
</head>
<body>
<main class="flyer">
  <section class="services">
    <h2 class="services__title">Our Services</h2>
    <p class="services__intro">We focus on both commercial and residential work. With us, no job is too big or too small.</p>
    <h3 class="services__subtitle">Our services include, but are not limited to:</h3>
    <ul class="service-list service-list--left">
      <li>General concreting</li>
      <li>Concreting for new homes or renovations</li>
      <li>Concreting for new home packages</li>
      <li>Footpaths</li>
      <li>Outdoor patios</li>
      <li>Concrete, timber and stone retaining walls</li>
      <li>Excavation, post hole digging and earth moving needs</li>
      <li>Exposed aggregate specialists</li>
    </ul>
    <ul class="service-list service-list--right">
      <li>Colour cove specialists</li>
      <li>Pool surrounds</li>
      <li>Landscaping</li>
      <li>Lawn and turf laying</li>
      <li>Quotes straight from plans</li>
      <li>Concrete removal</li>
      <li>Landscape design and construction</li>
      <li>Project management</li>
    </ul>
    <div class="pricing-band">
      <p>We usually charge per job and will always take<br>everything into consideration to give you a fair<br>and accurate quote.</p>
    </div>
    <div class="photo photo--lawn" role="img" aria-label="Photo of a freshly laid lawn in front of a new house"></div>
    <div class="photo photo--path" role="img" aria-label="Photo of a new patterned concrete pathway beside a brick home"></div>
    <div class="photo photo--deck" role="img" aria-label="Photo of a timber deck with a stepping stone and pebble garden path"></div>
  </section>

  <svg class="contact-circle" width="800" height="1128" viewBox="0 0 800 1128" aria-hidden="true">
    <defs>
      <linearGradient id="circleFill" x1="0" y1="0" x2="0" y2="1">
        <stop offset="0" stop-color="#00b3a8"/>
        <stop offset="1" stop-color="#0b8a76"/>
      </linearGradient>
    </defs>
    <circle cx="157" cy="1006" r="312" fill="url(#circleFill)" stroke="#ffffff" stroke-width="4"/>
  </svg>

  <p class="contact-copy contact-copy--chat">We are always happy to discuss your<br>plans and ideas. Get in touch with us<br>and have a chat about what the job<br>is, what needs to be done and your<br>preferred timeframe and we will work<br>in conjunction with you to get you the<br>results you desire.</p>
  <p class="contact-copy contact-copy--budget">We will always try to work within your<br>budget where possible. All our prices are<br>based on current market rates. We are also<br>happy to assist our clients in getting other<br>work done, since we have great working<br>relationships with our suppliers and a range of<br>different trades. We really are a one stop shop.</p>

  <svg class="chevrons" width="56" height="86" viewBox="0 0 56 86" aria-hidden="true">
    <polygon points="0,0 12,0 36,43 12,86 0,86 24,43" fill="#7fd6cd"/>
    <polygon points="20,0 32,0 56,43 32,86 20,86 44,43" fill="#7fd6cd"/>
  </svg>

  <div class="hours">
    <p class="hours__lead">Our current hours are</p>
    <p class="hours__time">6.30AM - 8.30PM<br>7 DAYS PER WEEK.</p>
    <p class="hours__note">We are very flexible with<br>our schedule.</p>
  </div>

  <div class="social">
    <span class="social__mark"></span>
    <span class="social__link">social.example/Morvasta-<br>Constructions-Pty-Ltd-/</span>
  </div>
</main>
</body>
</html>
```